Larkspur Ridge Management - Business Cards

I need business cards. My current logo was designed by a designer at this site and I very much like and am happy with the results. I would like a business card that is trendy, unique, current yet professional. I deal with high net worth clients daily

Target Market(s)

Out of state investors looking to get into the rental market in Ohio

Industry/Entity Type

Property Management, Consulting

Contact Information for Business Card

Name, Title (Chief Financial Officer) office phone number (555) 817-3094 website address larkridgemgmt.example

Font styles to use
Sans Serif

Colors
0054AA
0677BA
7BADD7
CADEEF
E8F1F8
0094D4
00A9DD
6FCCEA
C7EBF8
E9F6FB
00AB8E
00BBA5
67D7C9
C6EFE9
E9F9F6

```html
<!DOCTYPE html>
<html lang="en">
<head>
<meta charset="utf-8">
<title>Larkspur Ridge Management – Business Cards</title>
<link rel="stylesheet" href="https://fonts.googleapis.com/css2?family=Work+Sans:wght@400;500;700;800&display=swap">
<style>
  :root {
    --backdrop: #a9a9a9;
    --card: #ffffff;
    --navy: #1f3360;
    --red: #a51e22;
    --ink: #2a2a2a;
    --shadow: rgba(0, 0, 0, 0.28);
  }
  * { box-sizing: border-box; margin: 0; padding: 0; }
  html, body {
    width: 1200px;
    height: 1164px;
    overflow: hidden;
    background: var(--backdrop);
    font-family: "Work Sans", Arial, sans-serif;
  }
  .sheet {
    width: 1200px;
    height: 1164px;
    display: flex;
    flex-direction: column;
    align-items: center;
    justify-content: center;
    gap: 44px;
  }
  .card {
    width: 900px;
    height: 512px;
    background: var(--card);
    border-radius: 44px;
    box-shadow: 0 4px 10px var(--shadow);
    display: flex;
    align-items: center;
    justify-content: center;
  }
  .brand {
    display: flex;
    align-items: center;
    gap: 18px;
  }
  .brand-square {
    width: 34px;
    height: 34px;
    background: var(--navy);
  }
  .brand-name {
    font-size: 38px;
    font-weight: 800;
    color: var(--navy);
    letter-spacing: 0.2px;
  }
  .card-back { gap: 0; }
  .identity { text-align: left; }
  .identity-name {
    font-size: 40px;
    font-weight: 700;
    color: var(--red);
    letter-spacing: 0.5px;
    line-height: 1.1;
  }
  .identity-role {
    margin-top: 6px;
    font-size: 23px;
    font-weight: 400;
    color: var(--ink);
    letter-spacing: 0.6px;
  }
  .divider {
    width: 3px;
    height: 72px;
    background: var(--navy);
    margin: 0 46px 0 48px;
  }
  .contact {
    list-style: none;
    font-size: 23px;
    font-weight: 400;
    color: var(--ink);
    letter-spacing: 0.6px;
    line-height: 1.6;
  }
</style>
</head>
<body>
  <main class="sheet">
    <section class="card card-front" aria-label="Card front">
      <div class="brand">
        <span class="brand-square" aria-hidden="true"></span>
        <span class="brand-name">Larkspur Ridge Management</span>
      </div>
    </section>

    <section class="card card-back" aria-label="Card back">
      <div class="identity">
        <p class="identity-name">NAME, TITLE</p>
        <p class="identity-role">Chief Financial Officer</p>
      </div>
      <span class="divider" aria-hidden="true"></span>
      <ul class="contact">
        <li class="contact-phone">(555) 817-3094</li>
        <li class="contact-web">larkridgemgmt.example</li>
      </ul>
    </section>
  </main>
</body>
</html>
```